New furniture company needs a cool, fresh Website - think lounjo.com, velmora.com

Tuftwell.com: We are launching a home (Storvane) furniture business, aimed at the young, discerning mid-market consumer. The aim is to compete with many furniture e-tailers, as well as more established retail brands.
We want the website to capture the hearts, minds and wallets of the target audience, placing Tuftwell.com firmly into the market place. Please look to Velmora.com for look and feel inspiration. We will be selling approx 15 products to start. I suggest using Storvane with the following theme please: – Hearth & Meadow – Radiance – Belmont. Please see the logo below. The website needs to have a sophisticated feel for affordable aspirational furniture. Soft colours and homely text - please go with look and feel of Velmora.com. Please see a below file containing image of some sofas, chairs and footstools that will be for sale.
Many thanks

Target Market(s)

mid-market, young families looking for cool, affordable, easy to buy furniture

Industry/Entity Type

Furniture

Coding

Coded - Design and coding required

Number of Pages Required

5+ page

Font styles to use
Sans Serif

Colors
86cae7
cee9f5
3277b5
eaf2ce
fdf9ce
fff3d1
0255a3
e8e8e8
cbcbcb

Requirements
Must have
• Storvane
• http://www.velmora.com/hartwick-leather-large-sofa.html - great example of what we need it to look like
• logo as shown
• homepage
• products menu - sofas, seating, footstools, antique
• images of all products (examples provided) with ability to click on various fabric swatch samples and see the sofa in different fabrics and colours (check out lounjo.com)
• facility for social media
• facility to buy online
• "add to wishlist"
• "add to basket"
Nice to have
• I want it to have a light and airy feel, nothing too heavy or corporate. Needs to be very easily navigated and a simple approach
Should not have
• Dark, heavy colours

```html
<!DOCTYPE html>
<html lang="en">
<head>
<meta charset="utf-8">
<title>Contact Us – Tuftwell</title>
<link href="https://fonts.googleapis.com/css2?family=Roboto:wght@300;400;500&display=swap" rel="stylesheet">
<style>
:root{
  --ink:#1a1a1a;
  --text:#333;
  --muted:#9a9a9a;
  --line:#e8e8e8;
  --page-bg:#f2f2f2;
  --white:#fff;
  --sky:#86cae7;
  --blue:#3277b5;
  --brand:#777;
  --brand-mark:#d9d9d9;
}
*{box-sizing:border-box;margin:0;padding:0}
html,body{width:1130px;height:1200px;overflow:hidden;background:var(--white);font-family:'Roboto',sans-serif;color:var(--text)}
.canvas{position:relative;width:1130px;height:1200px}
a{color:inherit;text-decoration:none}

/* utility bar */
.utility-bar{position:absolute;top:0;left:0;width:100%;height:37px;border-bottom:1px solid var(--line);font-size:10.5px;color:#444}
.locale{position:absolute;left:82px;top:13px;display:flex;align-items:center;gap:6px}
.flag{width:13px;height:9px;background:#7d8db8;border:1px solid #c8c8c8}
.caret{width:0;height:0;border-left:3px solid transparent;border-right:3px solid transparent;border-top:4px solid #555;margin-left:4px}
.sep{width:1px;height:11px;background:#999;margin:0 12px}
.account-links{position:absolute;right:84px;top:0;height:37px;display:flex;align-items:center}
.account-links a{padding:0 12px;border-right:1px solid var(--line);line-height:18px}
.account-links a:last-child{border-right:0;padding-right:0}

/* main header */
.site-header{position:absolute;top:37px;left:0;width:100%;height:76px}
.brand{position:absolute;left:81px;top:14px;display:flex;flex-direction:column;align-items:flex-start;gap:8px}
.brand-mark{width:40px;height:26px;background:var(--brand-mark);margin-left:14px}
.brand-name{font-size:15px;font-weight:400;color:var(--brand);line-height:16px}
.main-nav{position:absolute;right:184px;top:33px;display:flex;gap:22px;font-size:10.5px;color:#333}
.header-tools{position:absolute;right:84px;top:26px;display:flex;align-items:center}
.tool-sep{width:1px;height:26px;background:var(--line);margin:0 14px}
.cart{position:relative}
.badge{position:absolute;top:-5px;right:-8px;width:12px;height:12px;border-radius:50%;background:#444;color:#fff;font-size:7.5px;display:flex;align-items:center;justify-content:center}

/* contact */
.contact{position:absolute;top:113px;left:0;width:100%;height:674px;background:var(--page-bg)}
.contact h1{position:absolute;top:102px;width:100%;text-align:center;font-size:30px;font-weight:400;color:#000}
.contact .lead{position:absolute;top:148px;width:100%;text-align:center;font-size:12.5px;line-height:18px;color:#222}
.contact-form{position:absolute;left:316px;top:205px;width:498px}
.field-label{display:block;font-size:12px;color:#222;margin:0 0 6px 1px}
.field{width:498px;height:42px;background:var(--white);border:1px solid var(--line);font-size:12px;color:var(--muted);padding:0 20px;display:flex;align-items:center;margin-bottom:18px}
.field.textarea{height:156px;align-items:flex-start;padding-top:16px;margin-bottom:10px}
.submit{width:116px;height:38px;background:var(--sky);color:#fff;font-size:11.5px;display:flex;align-items:center;justify-content:center}

/* newsletter */
.newsletter{position:absolute;top:787px;left:0;width:100%;height:100px;background:var(--sky)}
.newsletter h2{position:absolute;left:84px;top:36px;font-size:22.5px;font-weight:400;color:#fff}
.subscribe-form{position:absolute;left:641px;top:30px;display:flex}
.subscribe-input{width:298px;height:40px;background:#fff;font-size:12px;color:var(--muted);padding-left:18px;display:flex;align-items:center}
.subscribe-btn{width:107px;height:40px;background:var(--blue);color:#fff;font-size:11.5px;display:flex;align-items:center;justify-content:center}

/* footer */
.footer-cols{position:absolute;top:945px;left:0;width:100%}
.col{position:absolute;top:0}
.col h3{font-size:12.5px;font-weight:400;color:#000;margin-bottom:14px}
.col li{list-style:none;font-size:10.8px;color:#222;height:26px}
.social li{display:flex;align-items:center;gap:10px;height:29px}
.dot{width:25px;height:25px;border-radius:50%}
.footer-bottom{position:absolute;top:1148px;left:83px;width:963px;border-top:1px solid var(--line)}
.copyright{position:absolute;left:3px;top:22px;font-size:11px;color:#222}
.payments{position:absolute;right:-2px;top:12px;display:flex;gap:15px}
.pay{width:37px;height:24px;border-radius:4px;background:#f1f1f1;font-size:7px;color:#444;display:flex;align-items:center;justify-content:center}
</style>
</head>
<body>
<div class="canvas">

  <div class="utility-bar">
    <div class="locale">
      <span class="flag"></span><span>English</span><span class="caret"></span>
      <span class="sep"></span>
      <span>USD</span><span class="caret"></span>
    </div>
    <nav class="account-links">
      <a href="#">SITEMAP</a><a href="#">MY WISHLIST</a><a href="#">MY ACCOUNT</a><a href="#">MY CART</a><a href="#">SIGN IN</a>
    </nav>
  </div>

  <header class="site-header">
    <a class="brand" href="#">
      <span class="brand-mark" role="img" aria-label="Tuftwell brand mark"></span>
      <span class="brand-name">Tuftwell</span>
    </a>
    <nav class="main-nav">
      <a href="#">HOME</a><a href="#">CATEGORIES</a><a href="#">PRODUCTS</a><a href="#">FEATURES</a><a href="#">BLOG</a><a href="#">ABOUT US</a>
    </nav>
    <div class="header-tools">
      <svg width="16" height="16" viewBox="0 0 16 16" aria-label="Search"><circle cx="6.5" cy="6.5" r="5" fill="none" stroke="#86cae7" stroke-width="1.3"/><line x1="10.2" y1="10.2" x2="15" y2="15" stroke="#86cae7" stroke-width="1.3"/></svg>
      <span class="tool-sep"></span>
      <span class="cart">
        <svg width="17" height="18" viewBox="0 0 17 18" aria-label="Cart"><rect x="1" y="5" width="15" height="12" fill="none" stroke="#86cae7" stroke-width="1.3"/><path d="M5 7V4a3.5 3.5 0 0 1 7 0v3" fill="none" stroke="#86cae7" stroke-width="1.3"/></svg>
        <span class="badge">0</span>
      </span>
    </div>
  </header>

  <main class="contact">
    <h1>CONTACT US</h1>
    <p class="lead">This contact form is a dead end! If you really want to get in touch with us,<br>send an email to support@tuftwell.com</p>
    <form class="contact-form">
      <label class="field-label">Name :</label>
      <div class="field">your name</div>
      <label class="field-label">Email :</label>
      <div class="field">your mail</div>
      <label class="field-label">Message :</label>
      <div class="field textarea">description...</div>
      <div class="submit">SUBMIT</div>
    </form>
  </main>

  <section class="newsletter">
    <h2>SUBSCRIBE TO OUR NEWSLETTER</h2>
    <div class="subscribe-form">
      <div class="subscribe-input">Enter your email address</div>
      <div class="subscribe-btn">SUBSCRIBE</div>
    </div>
  </section>

  <footer class="footer-cols">
    <div class="col" style="left:81px"><h3>MY ACCOUNT</h3><ul><li>My Orders</li><li>My Vouchers</li><li>My Address</li><li>My Credit Slip</li><li>My History</li></ul></div>
    <div class="col" style="left:305px"><h3>INFORMATION</h3><ul><li>Contact Us</li><li>Search Terms</li><li>Shipping Guide</li><li>Term Of Use</li><li>Affiliate</li></ul></div>
    <div class="col" style="left:535px"><h3>EXTRA</h3><ul><li>Brand Partners</li><li>Gift Vouchers</li><li>Specials</li><li>Promotions</li><li>Whishlist</li></ul></div>
    <div class="col" style="left:745px"><h3>COLLECTION</h3><ul><li>Decorations</li><li>Living Room</li><li>Specials</li><li>Offical Care</li><li>Kitchen Care</li></ul></div>
    <div class="col" style="left:961px"><h3>FOLLOW US</h3>
      <ul class="social">
        <li><span class="dot" style="background:#3b5998"></span>Friendly</li>
        <li><span class="dot" style="background:#2aa3db"></span>Chirper</li>
        <li><span class="dot" style="background:#d63a2b"></span>Searchly +</li>
        <li><span class="dot" style="background:#1d4a80"></span>Linkly</li>
      </ul>
    </div>
  </footer>

  <div class="footer-bottom">
    <p class="copyright">2017 © Copyright . All rights reserved</p>
    <div class="payments">
      <span class="pay">Paywell</span><span class="pay">Vexa</span><span class="pay">Cardmo</span><span class="pay">Findr</span><span class="pay">Amexa</span><span class="pay">Mestra</span>
    </div>
  </div>

</div>
</body>
</html>
```